Natural Skincare Company Needs Label Design

We need a label design for the first product of a new company called 'Velo'. We make skincare products made from natural ingredients.
Our initial product is a rose hip oil, and we need a label for the small 30mL bottle that it comes in, as well as for the box that the bottle will be sold in. The label will be printed directly onto the bottle, like the example in the attached photo. For reference, we like the look and feel of the labels on the bottle and box in the attached photos. It should convey a sense of natural.
The bottle will be dark green glass. For the name 'Velo' we like something close to orange so that it stands out. The rest of the text on the front of the bottle and box should read 'natural skincare' 'pure & organic' 'Rose hip oil' 'huile de cynorrhodon' 'pure et biologique'. '30mL' '1fl.oz'
We also like the silhouette of the main ingredient like in the attached photo. So a silhouette of a rose hip on the front of the bottle and box would be preferred.
On the right side of the bottle and box:
'Rose hip oil'
'Ingredients: 100% natural, cold pressed, Rosa canina (rose hip) seed oil'
'Benefits: Hydrates and refreshes skin, leaving a more even skin tone and a healthy glow'
'Application: Massage 3-4 drops into clean, damp skin twice daily or as required'
'Suitable for all skin types'
'Store below 30C'
On the left side of the bottle and box:
'Huile de Cynorrhodon'
'Ingredients/Constituants: huile de Rosa canina (cynorrhodon) 100% naturel, presse a froid'
'Bienfaits: rafraichit la peau, teint eblouissant'
'Mode d'emploi: Massez 3 a 4 gouttes sur une peau propre et humide deluxe fois par jour'
'Convient a tous les types de peau'
'Conserver a moins de 30C'
Industry/Entity Type
It Company
Look and feel
Each slider illustrates characteristics of the customer's brand and the style your logo design should communicate.

```html
<!DOCTYPE html>
<html lang="en">
<head>
<meta charset="utf-8">
<title>Velo Rose Hip Oil – Box Dieline</title>
<link rel="stylesheet" href="https://fonts.googleapis.com/css2?family=Cinzel:wght@400;600&family=Merriweather:wght@400;700&display=swap">
<style>
  :root {
    --canvas: #ffffff;
    --green: #0a7443;
    --green-leaf: #4fa27a;
    --green-pattern: #268557;
    --brown: #331a04;
    --brown-pattern: #4a2e16;
    --hip-mauve: #9c8a82;
    --orange: #e8901f;
    --cream: #f3ece0;
    --rule: #b9d6c6;
  }
  * { margin: 0; padding: 0; box-sizing: border-box; }
  html, body { width: 1200px; height: 1000px; overflow: hidden; background: var(--canvas); }
  .dieline { position: relative; width: 1200px; height: 1000px; }
  .panel { position: absolute; }
  .top-flap { left: 246px; top: 33px; width: 356px; height: 232px; background: var(--green); }
  .side-fr  { left: 15px;  top: 265px; width: 231px; height: 552px; background: var(--brown); }
  .front    { left: 246px; top: 265px; width: 356px; height: 552px; background: var(--green); }
  .side-en  { left: 602px; top: 265px; width: 232px; height: 552px; background: var(--brown); }
  .back     { left: 834px; top: 265px; width: 356px; height: 552px;
              background: linear-gradient(160deg, var(--green-pattern), var(--green) 60%, var(--green-pattern)); }
  .side-pattern { position: absolute; inset: 0;
              background: linear-gradient(180deg, var(--brown-pattern), var(--brown) 50%, var(--brown-pattern)); opacity: .55; }

  .centered { position: absolute; left: 0; right: 0; text-align: center; }
  .sprig { position: absolute; border-radius: 45% 55% 40% 60%; }
  .sprig--green { background: radial-gradient(circle at 40% 45%, var(--green-leaf), rgba(79,162,122,.35) 70%, transparent 72%); }
  .sprig--mauve { background: radial-gradient(circle at 45% 45%, var(--hip-mauve), rgba(156,138,130,.35) 68%, transparent 70%); }

  .brand-name { font-family: "Cinzel", serif; font-weight: 400; color: var(--orange); line-height: 1; }
  .product-name { font-family: "Cinzel", serif; color: var(--orange); letter-spacing: .03em; line-height: 1; }
  .product-name--light { color: var(--cream); }
  .product-sub { font-family: "Cinzel", serif; color: var(--cream); letter-spacing: .08em; line-height: 1; }
  .tagline { font-family: "Cinzel", serif; font-weight: 600; color: var(--orange); letter-spacing: .2em; font-size: 12px; }
  .claim { font-family: "Cinzel", serif; color: var(--cream); letter-spacing: .14em; font-size: 13px; }
  .claim-rule { position: absolute; left: 62px; width: 224px; height: 1px; background: var(--rule); top: 453px; }
  .volume { font-family: "Cinzel", serif; font-weight: 600; color: var(--orange); letter-spacing: .1em; font-size: 13px; }

  .info { position: absolute; top: 238px; width: 150px; font-family: "Merriweather", serif;
          font-size: 8.6px; line-height: 15px; color: var(--cream); }
  .info p { margin-bottom: 14px; }
  .info strong { font-weight: 700; }
  .side-fr .info { left: 39px; }
  .side-en .info { left: 44px; }

  .web { font-family: "Cinzel", serif; color: var(--cream); letter-spacing: .1em; font-size: 13px; }
</style>
</head>
<body>
<main class="dieline">

  <section class="panel top-flap">
    <div class="sprig sprig--green" role="img" aria-label="Rose hip sprig silhouette" style="left:148px;top:26px;width:80px;height:110px;"></div>
    <div class="centered brand-name" style="top:128px;font-size:42px;">Velo</div>
    <div class="centered product-name" style="top:172px;font-size:17px;">Rose hip oil</div>
    <div class="centered product-sub" style="top:192px;font-size:8px;">huile de cynorrhodon</div>
  </section>

  <section class="panel side-fr">
    <div class="side-pattern" role="img" aria-label="Faint rose hip leaf pattern"></div>
    <div class="sprig sprig--mauve" role="img" aria-label="Rose hip sprig silhouette" style="left:92px;top:84px;width:72px;height:72px;"></div>
    <div class="centered brand-name" style="top:158px;font-size:30px;">Velo</div>
    <div class="centered product-sub" style="top:197px;font-size:10.5px;">Huile de cynorrhodon</div>
    <div class="info">
      <p><strong>Ingredients/Constituants:</strong> huile de Rosa canina (cynorrhodon) 100% naturel, presse a froid.</p>
      <p><strong>Bienfaits:</strong> rafraichit la peau, teint eblouissant.</p>
      <p><strong>Mode d'emploi:</strong> Massez 3 a 4 gouttes sur une peau propre et humide deluxe fois par jour.</p>
      <p><strong>Convient a tous les types de peau.</strong></p>
      <p><strong>Conserver a moins de 30C.</strong></p>
    </div>
  </section>

  <section class="panel front">
    <div class="sprig sprig--green" role="img" aria-label="Rose hip sprig silhouette" style="left:160px;top:45px;width:130px;height:165px;"></div>
    <div class="centered brand-name" style="top:200px;font-size:66px;">Velo</div>
    <div class="centered product-name" style="top:290px;font-size:29px;">Rose hip oil</div>
    <div class="centered product-sub" style="top:328px;font-size:12.5px;">huile de cynorrhodon</div>
    <div class="centered tagline" style="top:397px;">natural skincare</div>
    <div class="centered claim" style="top:432px;">PURE &amp; ORGANIC</div>
    <div class="claim-rule"></div>
    <div class="centered claim" style="top:461px;">PURE ET BIOLOGIQUE</div>
    <div class="centered volume" style="top:495px;">30ML 1FL.OZ</div>
  </section>

  <section class="panel side-en">
    <div class="side-pattern" role="img" aria-label="Faint rose hip leaf pattern"></div>
    <div class="sprig sprig--mauve" role="img" aria-label="Rose hip sprig silhouette" style="left:92px;top:84px;width:72px;height:72px;"></div>
    <div class="centered brand-name" style="top:158px;font-size:30px;">Velo</div>
    <div class="centered product-name product-name--light" style="top:196px;font-size:15px;">Rose hip oil</div>
    <div class="info">
      <p><strong>Ingredients</strong>: 100% natural, cold pressed, Rosa canina (rose hip) seed oil.</p>
      <p><strong>Benefits:</strong> Hydrates and refreshes skin, leaving a more even skin tone and a healthy glow.</p>
      <p><strong>Application:</strong> Massage 3-4 drops into clean, damp skin twice daily or as required.</p>
      <p><strong>Suitable for all skin types.</strong></p>
      <p><strong>Store below 30C.</strong></p>
    </div>
  </section>

  <section class="panel back" role="img" aria-label="Rose hip leaves and berries pattern">
    <div class="centered web" style="top:504px;">WWW.VELONATURAL.COM</div>
  </section>

</main>
</body>
</html>
```